Birchfield Vacation Rentals Bill Board

7x21 bill board.

Im needing a bill board for a vacation rental company. Specializing in cabin rentals.
Here are the main points I want mentioned on the billboard:

Quality vacation rentals

Accepting new vacation rental homes.

Family owned and operated.

Birchfieldvr.example
555-318-7042

Use either logo whichever looks best. Be creative

Target Market(s)

Cabin owners

Industry/Entity Type

Hospitality

Font styles to use
Sans Serif

Requirements
Must have
• Would like the cabin picture to be the background. Must have the birchfield logo, phone number and website

```html
<!DOCTYPE html>
<html lang="en">
<head>
<meta charset="utf-8">
<title>Birchfield Vacation Rentals Billboard</title>
<link href="https://fonts.googleapis.com/css2?family=Poppins:wght@400;500;600;700&display=swap" rel="stylesheet">
<style>
  :root {
    --navy: #1e2f45;
    --navy-deep: #16243a;
    --sage: #7f9c77;
    --sage-text: #8fae84;
    --white: #ffffff;
    --page: #eef1f4;
    --sky-top: #f2a15a;
    --sky-mid: #9a6a52;
    --wood: #5a3a24;
  }
  html, body { margin: 0; padding: 0; overflow: hidden; }
  body {
    width: 1200px; height: 1200px;
    background: var(--page);
    display: flex; align-items: center; justify-content: center;
    font-family: "Poppins", sans-serif;
  }
  .billboard {
    position: relative;
    width: 1140px; height: 380px;
    background: var(--navy);
    overflow: hidden;
    box-shadow: 0 10px 30px rgba(0,0,0,.18);
  }
  .cabin-photo {
    position: absolute; left: 430px; top: 0; width: 710px; height: 300px;
    background: linear-gradient(180deg, var(--sky-top) 0%, var(--sky-mid) 35%, var(--wood) 70%, #2c2a2e 100%);
  }
  .cabin-photo::after {
    content: ""; position: absolute; inset: 0;
    background: linear-gradient(90deg, var(--navy) 0%, rgba(30,47,69,.6) 18%, rgba(30,47,69,0) 40%);
  }
  .shapes { position: absolute; inset: 0; }
  .headline-banner {
    position: absolute; left: 470px; top: 62px; width: 650px; height: 72px;
    display: flex; align-items: center; justify-content: center;
    color: var(--white); font-weight: 700; font-size: 38px; letter-spacing: .5px;
    line-height: 1; white-space: nowrap;
  }
  .brand {
    position: absolute; left: 40px; top: 72px;
    color: var(--white); font-weight: 600; font-size: 28px; letter-spacing: .5px;
  }
  .offer {
    position: absolute; left: 40px; top: 126px;
    color: var(--sage-text); font-weight: 500; font-size: 31px; line-height: 1.25;
  }
  .offer-rule {
    position: absolute; left: 40px; top: 212px; width: 330px; height: 2px; background: var(--white);
  }
  .tagline {
    position: absolute; left: 40px; top: 228px;
    color: var(--white); font-weight: 400; font-size: 18px;
  }
  .book-now {
    position: absolute; left: 28px; top: 330px;
    background: var(--navy-deep); color: var(--white);
    font-weight: 600; font-size: 19px; line-height: 1; padding: 9px 12px; border-radius: 6px;
  }
  .phone {
    position: absolute; left: 180px; top: 321px;
    color: var(--white); font-weight: 700; font-size: 38px; line-height: 1.2;
  }
  .website {
    position: absolute; left: 610px; top: 292px;
    color: var(--white); font-weight: 400; font-size: 36px; line-height: 1.2;
  }
</style>
</head>
<body>
  <div class="billboard">
    <div class="cabin-photo" role="img" aria-label="Log cabin with a wraparound deck on a mountainside at sunset"></div>
    <svg class="shapes" width="1140" height="380" viewBox="0 0 1140 380" aria-hidden="true">
      <polygon points="450,62 1140,62 1140,134 474,134" fill="var(--navy-deep)"/>
      <polygon points="0,316 470,316 500,380 0,380" fill="var(--sage)"/>
      <polygon points="500,288 1140,288 1140,346 522,346" fill="var(--navy)"/>
      <polygon points="522,346 1140,346 1140,380 536,380" fill="var(--sage)"/>
    </svg>
    <div class="headline-banner">QUALITY VACATION RENTALS</div>
    <div class="brand">Birchfield Vacation Rentals</div>
    <div class="offer">Accepting New<br>Vacation Rental Homes</div>
    <div class="offer-rule"></div>
    <div class="tagline">Family Owned and Operated</div>
    <div class="book-now">BOOK NOW!</div>
    <div class="phone">555-318-7042</div>
    <div class="website">birchfieldvr.example</div>
  </div>
</body>
</html>
```